Copper Vale Winery wants innovative label for unique bottling

We are looking for a lable for a champagne which is made of Eiswein (Ice Wine; this is what you get when you harvest the grapes at temperatures below -7 degrees celsius. the water is frozen and you only get the pure extract out of the grapes (sugar, acid and all the aromas). even after fermentation is remains very sweet. we then turned it into champagne (2nd fermentation in bottles for another 12 months and so on and so forth). It is bottled in small champagne bottles (0,375 l). Dark green (just like a champagne bottle). The name of the product is "Glintova" (from Freeze and Riesling). So it is unique, it is sparkling, it is sweet, it is full of aromas and it is produced from deep frozen grapes. All of this hopefully creates ideas in your imagination which lead to great designs! The only word printed onto the label is "Glintova". The colour code should still be recognizable. See www.brandt-wolmer.de for our standard labels and bottles. you can also download label designs and colours. we prefer modern / fresh / light design rather than traditional, flowery, pittoresque. But please not 100 different colours or screaming colours. You may also imagine transparent labels. Up to you! Have fun!

```html
<!DOCTYPE html>
<html lang="de">
<head>
<meta charset="utf-8">
<title>Glintova – Eiswein Label</title>
<link href="https://fonts.googleapis.com/css2?family=Pinyon+Script&family=Roboto:wght@700&family=Tinos:ital@1&display=swap" rel="stylesheet">
<style>
  :root {
    --frame-light: #dfe6ef;
    --frame-mid: #9fb2cb;
    --frame-blue: #5f7fae;
    --frame-dark: #1e3b70;
    --panel: #ffffff;
    --panel-edge: #2b4677;
    --script-ink: #4d5d7c;
    --text-ink: #111111;
  }

  html, body {
    margin: 0;
    padding: 0;
    width: 828px;
    height: 1200px;
    overflow: hidden;
    background: #ffffff;
  }

  .label {
    position: relative;
    width: 828px;
    height: 1200px;
    box-sizing: border-box;
    background:
      linear-gradient(180deg, rgba(255,255,255,0.35) 0%, rgba(255,255,255,0) 35%, rgba(20,40,90,0.25) 100%),
      linear-gradient(90deg,
        var(--frame-mid) 0%,
        var(--frame-light) 14%,
        var(--frame-mid) 38%,
        var(--frame-blue) 68%,
        var(--frame-dark) 100%);
  }

  .label__panel {
    position: absolute;
    left: 33px;
    top: 33px;
    right: 33px;
    bottom: 33px;
    background: var(--panel);
    border: 2px solid var(--panel-edge);
    box-sizing: border-box;
  }

  .label__name {
    position: absolute;
    left: 0;
    right: 0;
    top: 395px;
    margin: 0;
    text-align: center;
    font-family: "Pinyon Script", cursive;
    font-weight: 400;
    font-size: 150px;
    line-height: 1;
    color: var(--script-ink);
  }

  .label__variety {
    position: absolute;
    left: 0;
    right: 0;
    top: 1000px;
    margin: 0;
    text-align: center;
    font-family: "Roboto", Arial, sans-serif;
    font-weight: 700;
    font-size: 37px;
    line-height: 1;
    color: var(--text-ink);
  }

  .label__volume {
    position: absolute;
    right: 32px;
    top: 1060px;
    margin: 0;
    font-family: "Tinos", "Times New Roman", serif;
    font-style: italic;
    font-size: 36px;
    line-height: 1;
    color: var(--text-ink);
  }
</style>
</head>
<body>
  <main class="label">
    <section class="label__panel">
      <h1 class="label__name">Glintova</h1>
      <p class="label__variety">Eiswein</p>
      <p class="label__volume">0,375 l</p>
    </section>
  </main>
</body>
</html>
```